July 2022 Industrial Manufacturer Product Expo Mexico City

We manufacture large screws and fastners for large Mining equipment, Trains, large ships, airplanes, wind turbines, and so on. We also do custom work base on the customer needs. No matter the size we can make it.
We have a Expo coming up with companies all over the world. We have to stand out we are a family own business so our customer service will be above and beyond anyone can provide. We do not have a sales force to push our products and services we provide one on one service.
Plus@!! I'm looking for anything that you designers can come up with if it was your company to put on a business card, plus i want to do a 1 or 2 sided pamphlet, and then a website. We make Speciality Bolts for large mining equipment these bolts can be 3 to 4 foot long!!! Plus fasteners, Nuts, washers, any, size, strengths, special materials, we offer more of a ono on one customer service, We are a small company, family own, but can fulfill any type of orders. We can also provide special time lines for emergency orders. "We keep the machines running we here at RWK don't believe in down time" We want to hear any slogan based on our company to stand out.
Thanks i really appreciate all your work and options that we have to pick on. Plus just a thought we could possibly want to entertain a experience Marketing internet help maybe a employment possibility. Thanks
Updates

I need 2 cards one in Spanish and English Like the steel back ground maybe send me in some bright red and blue writing Same with the Black cards Please remove the word Military The logo RWK maybe integrate a picture of a Bolt 🔩 Thank you

Still looking for I need 2 cards one in Spanish and English Like the steel back ground maybe send me in some bright red and blue writing Same with the Black cards try bright writing Please remove the word Military The logo RWK maybe integrate a picture of a Bolt 🔩 Plus will need the company to make a brochure and website next Thank you

Target Market(s)

Large Mining, Ship, Train, Green Energy, OPRE, and Government equipment. Throughout the World

Industry/Entity Type

We can Custom Manufacture any type of Fastners for Mining equipment, Trains, Ships, Green energy, Governments, or military projects. wind turbines,

Contact Information for Business Card

I attached the name and contact info that's on a card, plus the Company Logo. Would like industrial looking background with Bright Colors that will stand out!! If we can insert somewhere maybe on back that we "Custom Manufacture Any Size or Quantity Fastners for Large Mining Equipment, Trains, Ships, Green Energy Equipment or Government Projects

Font styles to use
Other font styles liked:
• You Pick, has to be bold, colorful standout, Professional looking Beable to read it.

Colors

Designer to choose colors to be used in the design.

Requirements
Must have
• Need in Spanish and English TO STANDOUT FROM THE REST OF THE EXPO!! See Business card details, Rounded corners
Nice to have
• Can i see some of the darker cards with Bright Red and Blue letters I like to see the different type of card material, heavy thickness, plastic, transparent, Metal types, Bright Colors, I saw like Raised letters like on the logo.

```html
<!DOCTYPE html>
<html lang="es">
<head>
<meta charset="utf-8">
<title>RWK – Tarjeta de presentación</title>
<link rel="stylesheet" href="https://fonts.googleapis.com/css2?family=Roboto+Condensed:wght@300;400;700&family=Oswald:wght@500&display=swap">
<style>
  :root {
    --page-bg: #d9d4cc;
    --card-frost: #e6e2dc;
    --card-frost-edge: #cfcac2;
    --ink-dark: #1d1d24;
    --ink-navy: #1a2a6b;
    --band-blue: #1f4fa6;
    --band-navy: #06103f;
    --stripe-black: #141414;
    --stripe-light: #efe7da;
    --text-light: #e9e4da;
  }
  html, body {
    margin: 0;
    padding: 0;
    width: 1200px;
    height: 969px;
    overflow: hidden;
    background: var(--page-bg);
  }
  .card {
    position: absolute;
    left: 184px;
    top: 226px;
    width: 868px;
    height: 494px;
    border-radius: 26px;
    overflow: hidden;
    background: linear-gradient(160deg, #eeebe6 0%, var(--card-frost) 50%, var(--card-frost-edge) 100%);
    box-shadow: 0 0 0 1px rgba(255,255,255,0.6) inset, 0 12px 30px rgba(0,0,0,0.18);
    font-family: "Roboto Condensed", sans-serif;
  }
  .card__bands {
    position: absolute;
    inset: 0;
    width: 100%;
    height: 100%;
  }
  .brand {
    position: absolute;
    left: 72px;
    top: 56px;
    margin: 0;
    display: flex;
    align-items: center;
    gap: 18px;
    font-weight: 700;
    font-size: 112px;
    line-height: 1;
    letter-spacing: 6px;
    color: var(--ink-dark);
  }
  .brand__dot {
    width: 22px;
    height: 22px;
    border-radius: 50%;
    background: var(--band-blue);
  }
  .tagline {
    position: absolute;
    left: 72px;
    top: 170px;
    margin: 0;
    font-size: 25px;
    font-weight: 400;
    color: var(--ink-navy);
    letter-spacing: 0.2px;
  }
  .contact {
    position: absolute;
    right: 50px;
    top: 328px;
    text-align: right;
    color: var(--text-light);
  }
  .contact__name {
    margin: 0;
    font-family: "Oswald", sans-serif;
    font-weight: 500;
    font-size: 24px;
    line-height: 1.1;
    letter-spacing: 0.3px;
  }
  .contact__role {
    margin: 2px 0 0;
    font-size: 18px;
    font-weight: 300;
  }
  .contact__line {
    margin: 0;
    font-size: 20px;
    font-weight: 300;
    display: flex;
    justify-content: flex-end;
    align-items: center;
    gap: 6px;
  }
  .contact__line--phones { margin-top: 20px; }
  .contact__line--email { margin-top: 4px; }
  .icon { width: 16px; height: 16px; fill: var(--text-light); }
  .icon--gap { margin-left: 8px; }
</style>
</head>
<body>
  <div class="card">
    <svg class="card__bands" viewBox="0 0 868 494" preserveAspectRatio="none" aria-hidden="true">
      <defs>
        <linearGradient id="bandFill" x1="0" y1="0" x2="1" y2="1">
          <stop offset="0" stop-color="#2a5db5"/>
          <stop offset="0.55" stop-color="#123683"/>
          <stop offset="1" stop-color="#06103f"/>
        </linearGradient>
      </defs>
      <polygon points="0,389 868,157 868,169 0,401" fill="var(--stripe-black)"/>
      <polygon points="0,401 868,169 868,174 0,406" fill="var(--stripe-light)"/>
      <polygon points="0,406 868,174 868,494 0,494" fill="url(#bandFill)"/>
    </svg>

    <h1 class="brand"><span class="brand__name">RWK</span><span class="brand__dot"></span></h1>
    <p class="tagline">FABRICACION Y DISTRIBUCION DE TORNILLOS</p>

    <div class="contact">
      <p class="contact__name">Lic. Mariela Ofelia Durán Ríos</p>
      <p class="contact__role">Cotizaciones en</p>
      <p class="contact__line contact__line--phones">
        <svg class="icon" viewBox="0 0 16 16"><path d="M3.5 1.5l2.5 0 1 3.5-1.8 1.2c.8 1.8 2.2 3.2 4 4l1.2-1.8 3.5 1v2.5c0 .8-.7 1.5-1.5 1.5C6.6 13.4 2.6 9.4 2 3c0-.8.7-1.5 1.5-1.5z"/></svg>
        <span>5550142301</span>
        <svg class="icon icon--gap" viewBox="0 0 16 16"><path d="M4.5 0.5h7a1 1 0 0 1 1 1v13a1 1 0 0 1-1 1h-7a1 1 0 0 1-1-1v-13a1 1 0 0 1 1-1zm.6 1.8v10h5.8v-10zm2.9 10.8a.7.7 0 1 0 0 1.4.7.7 0 0 0 0-1.4z"/></svg>
        <span>5550187622</span>
      </p>
      <p class="contact__line contact__line--email">
        <svg class="icon" viewBox="0 0 16 16"><path d="M1 4h14v9H1zM1.8 4.6 8 9l6.2-4.4v1L8 10 1.8 5.6z" fill-rule="evenodd"/></svg>
        <span>ventas.rwktornillos@example.com</span>
      </p>
    </div>
  </div>
</body>
</html>
```